Flyer design for Wander With Us Outback Trips

We need a new flyer for our tour business. Sketch horde produced a great flyer for us 4 years ago but it is time to update. We have had a price increase that needs to be reflected but we have noticed an issue with our current marketing.
Our tour is a "tagalong" tour which means you follow in your own vehicle. Unfortunately most people associate "tagalong" with 4wd (Four wheel drive vehicles). This is not the case for our tour which can be done in ANY type of vehicle. We need to get across at first glance that this tour is available to all vehicle types. We also need to stress that there is NOT MUCH DRIVING. We cover around 20km total of very easy driving. We go from point of interest to point of interest.
We want our customers to feel that this tour will be a better option than selecting a bus type tour because they use their own vehicle. Our option is also MUCH cheaper than bus options but provides a premium product. It's "cheap" but not cheap if you understand.
I will upload our previous flyer so you have an idea of what we do and how we have been presenting it. We are currently single sided DL but do not mind if we go into double sided DL if you feel that will enable you to share more information. Our price is $50 and half price for kids (as per old flyer)
Some things to remember when trying to appeal to our customer:
Choose a design that clearly communicates that our tagalong tour is suitable for all types of vehicles. For example, "Vehicle-Friendly Tagalong Tour" or "All-Vehicle Tagalong Tour".
Use clear language: Avoid using terms like "off-road" or "4x4" that may imply that our tour is only suitable for certain types of vehicles. Instead, use language that is inclusive and clearly communicates that all vehicles are welcome.
Include photos and videos of a variety of vehicles: This will show potential customers that our tagalong tour is not limited to four-wheel drive vehicles and that any type of vehicle can participate.
Highlight the benefits of a tagalong tour over a bus tour: Emphasise the flexibility and freedom that a tagalong tour offers, as well as the opportunity to explore off-the-beaten-path destinations that are not accessible by bus.
By incorporating these elements into your product presentation, you can avoid confusion and clearly communicate that our tagalong tour is suitable for any type of vehicle, while also highlighting the unique benefits of this type of tour.
Along with the emphasis on all vehicles you need to be clear about what we offer on the tour.
- The excitement of an opal mine tour with an award winning guide and opal miner.
- The wonder of an underground home and discovering how people live in an underground environment.
- Driving through the opal mining area for a close up view of the field.
- Our EXCLUSIVE opal cutting and polishing demonstration.
- The adventure of looking for your own opal.
For further information visit our web site "http://wanderwithus.outback.example". Check our facebook page "https://www.facebook.com/wanderwithusoutbacktrips". Search Google for "Coober Pedy", Wander with us Coober Pedy" or "Coober Pedy Opal mining" to source images of our town and opals.
PLEASE ALSO FIND SOMEWHERE TO SAY "FREE UNPOWERED CAMPING AT TOLMA'S WITH ALL TOURS AS WELL AS DISCOUNTS ON POWERED CAMPING" and make this stand out somehow. (http://rest-belowground.example.au)

Target Market(s)

18 to 80

Industry/Entity Type

Tourism

Font styles to use
Serif

Colors

Designer to choose colors to be used in the design.

Requirements
Must have
• Eye catching images and attention grabbing headlines
Nice to have
• Modern design.
Should not have
• References to 4wd or buses.

```html
<!DOCTYPE html>
<html lang="en">
<head>
<meta charset="utf-8">
<title>Wander With Us Outback Trips – All-Vehicle Tagalong Tour Flyer</title>
<link rel="stylesheet" href="https://fonts.googleapis.com/css2?family=Zilla+Slab:ital,wght@0,500;0,600;0,700;1,700&family=Lora:wght@400;500&display=swap">
<style>
  :root{
    --cream:#fdf3ea;
    --orange:#ef8a1c;
    --orange-dark:#e8741a;
    --amber:#f2a900;
    --peach:#f8b874;
    --ink:#3b3b3b;
    --ink-soft:#2b2b2b;
    --charcoal:#333333;
    --ring:#8c8c8c;
    --white:#ffffff;
    --shade:rgba(20,40,70,.55);
  }
  *{margin:0;padding:0;box-sizing:border-box}
  html,body{width:1200px;height:2542px;overflow:hidden;background:var(--cream)}
  .flyer{position:relative;width:1200px;height:2542px;overflow:hidden;font-family:"Lora",serif;color:var(--ink)}
  .backdrop{position:absolute;inset:0}

  .hero-message{position:absolute;left:60px;top:60px;width:760px;padding:26px 34px;background:var(--shade);border-left:10px solid var(--amber);color:var(--white)}
  .hero-message h1{font-family:"Zilla Slab",serif;font-weight:700;font-size:62px;line-height:64px;letter-spacing:.5px}
  .hero-message p{font-family:"Zilla Slab",serif;font-weight:500;font-size:30px;line-height:38px;margin-top:12px}

  .join-badge{position:absolute;left:727px;top:694px;width:270px;height:270px;border-radius:50%;background:var(--orange);
    display:flex;flex-direction:column;justify-content:center;align-items:center;font-family:"Zilla Slab",serif;font-weight:700;color:var(--peach);line-height:.95;text-align:center}
  .join-badge .small{font-size:44px}
  .join-badge .big{font-size:56px}
  .join-badge .price{font-size:24px;color:var(--white);margin-top:10px;line-height:28px}

  .feature{position:absolute;left:172px;width:950px}
  .feature h2{font-family:"Zilla Slab",serif;font-weight:600;font-size:38px;line-height:44px;color:var(--ink);margin-bottom:6px}
  .feature p{font-size:27px;line-height:41px;font-weight:400}
  .feature-icon{position:absolute;left:67px;width:72px;height:72px}

  .camping-banner{position:absolute;left:68px;top:2001px;width:1087px;height:210px}
  .camping-text{position:absolute;left:140px;top:2016px;font-family:"Zilla Slab",serif;font-style:italic;font-weight:700;font-size:37px;line-height:46px;color:var(--white)}
  .camping-link{position:absolute;left:140px;top:2118px;font-family:"Zilla Slab",serif;font-style:italic;font-weight:700;font-size:38px;color:var(--white)}

  .brand{position:absolute;left:331px;top:2248px;width:148px;height:148px;border-radius:50%;background:var(--orange);
    display:flex;align-items:center;justify-content:center;text-align:center;font-family:"Zilla Slab",serif;font-weight:600;font-size:24px;line-height:26px;color:var(--white)}
  .contacts{position:absolute;left:553px;top:2243px;list-style:none}
  .contacts li{display:flex;align-items:center;height:38px;font-family:"Zilla Slab",serif;font-weight:600;font-size:30px;color:var(--ink-soft)}
  .contacts svg{width:26px;height:26px;margin-right:28px;flex:none}
  .follow-bar{position:absolute;left:596px;top:2377px;width:538px;height:57px;background:var(--orange);border-radius:0 40px 40px 0;
    display:flex;align-items:center;padding-left:14px;font-family:"Zilla Slab",serif;font-weight:600;font-size:38px;color:var(--white)}
  .follow-bar .social{width:44px;height:44px;border:3px solid var(--white);border-radius:8px;margin-left:12px}
  .follow-bar .social:first-of-type{margin-left:80px}
</style>
</head>
<body>
<main class="flyer">
  <svg class="backdrop" width="1200" height="2542" viewBox="0 0 1200 2542">
    <defs>
      <linearGradient id="warmWash" x1="0" y1="0" x2="1" y2="1">
        <stop offset="0" stop-color="#fbe3cc"/><stop offset=".5" stop-color="#fdf4ec"/><stop offset="1" stop-color="#fdf2ea"/>
      </linearGradient>
      <linearGradient id="photoTone" x1="0" y1="0" x2="0" y2="1">
        <stop offset="0" stop-color="#2f72c9"/><stop offset=".4" stop-color="#8db8e6"/><stop offset=".55" stop-color="#b7b2a6"/><stop offset=".75" stop-color="#b48a64"/><stop offset="1" stop-color="#a9784f"/>
      </linearGradient>
      <linearGradient id="bannerTone" x1="0" y1="0" x2="1" y2="0">
        <stop offset="0" stop-color="#e8501f"/><stop offset=".5" stop-color="#ef7a1c"/><stop offset="1" stop-color="#f08a1c"/>
      </linearGradient>
    </defs>
    <rect width="1200" height="2542" fill="url(#warmWash)"/>
    <polygon role="img" aria-label="Photo: a line of everyday cars, vans and utes parked on red outback ground in Coober Pedy under a blue sky" points="0,0 1200,0 1200,905 0,545" fill="url(#photoTone)"/>
    <polygon points="0,570 687,765 687,815 0,628" fill="var(--amber)"/>
    <polygon points="0,628 687,815 687,838 0,650" fill="var(--orange-dark)"/>
    <polygon points="157,745 402,830 402,897 157,818" fill="var(--peach)"/>
    <polygon points="194,735 400,796 400,862 194,800" fill="var(--white)"/>
    <polygon points="1035,872 1200,920 1200,966 1035,920" fill="var(--amber)"/>
    <polygon points="1035,920 1200,966 1200,988 1035,940" fill="var(--orange-dark)"/>
    <path d="M0,2180 Q30,2470 440,2478 L1200,2478 L1200,2542 L0,2542 Z" fill="var(--charcoal)"/>
    <path d="M0,2180 Q30,2470 440,2478 L1200,2478" fill="none" stroke="#bdbdbd" stroke-width="6"/>
  </svg>

  <header class="hero-message">
    <h1>ALL-VEHICLE<br>TAGALONG TOUR</h1>
    <p>Any car, ute, van or camper welcome.<br>Only about 20km of easy driving in total.</p>
  </header>

  <div class="join-badge"><span class="small">JOIN US</span><span class="big">TODAY</span><span class="price">$50 adults<br>kids half price</span></div>

  <svg class="feature-icon" style="top:940px" viewBox="0 0 72 72"><circle cx="36" cy="36" r="32" fill="#fff" stroke="var(--ring)" stroke-width="5"/><path d="M20 40 a16 16 0 0 1 32 0 z" fill="var(--orange)"/><rect x="18" y="40" width="36" height="5" fill="var(--orange)"/></svg>
  <section class="feature" style="top:928px"><h2>SAFETY GEAR</h2><p>A safety gear will be provided for you including helmet and UHF radios. Your safety is our number one priority!</p></section>

  <svg class="feature-icon" style="top:1080px" viewBox="0 0 72 72"><circle cx="36" cy="36" r="32" fill="#fff" stroke="var(--ring)" stroke-width="5"/><path d="M18 36 L36 20 L54 36 L50 36 L50 52 L22 52 L22 36 Z" fill="var(--orange)"/></svg>
  <section class="feature" style="top:1070px"><h2>UNDERGROUND HOME</h2><p>Our guide will show you through a miners dugout. See how people live underground andlearn why, as you experience underground living first hand.</p></section>

  <svg class="feature-icon" style="top:1278px" viewBox="0 0 72 72"><circle cx="36" cy="36" r="32" fill="#fff" stroke="var(--ring)" stroke-width="5"/><rect x="31" y="22" width="10" height="30" fill="var(--orange)"/><rect x="22" y="20" width="28" height="6" fill="var(--orange)"/></svg>
  <section class="feature" style="top:1266px"><h2>OPAL MINING</h2><p>We’ll make our way down an underground mine where we’ll show you the different techniques that modern miners use to extract this beautiful stone.</p></section>

  <svg class="feature-icon" style="top:1470px" viewBox="0 0 72 72"><circle cx="36" cy="36" r="32" fill="#fff" stroke="var(--ring)" stroke-width="5"/><rect x="18" y="38" width="26" height="10" rx="3" fill="var(--orange)"/><rect x="44" y="24" width="8" height="24" fill="var(--orange)"/></svg>
  <section class="feature" style="top:1462px"><h2>DRIVE THROUGH THE FIELD</h2><p>Making our way into town, via the opal fields, you’ll get a front row seat for viewing our magical landscape that has been terraformed with over 100 years of mining. We might even popinto Cooper Pedy’s world famous golf course on our way!</p></section>

  <svg class="feature-icon" style="top:1710px" viewBox="0 0 72 72"><circle cx="36" cy="36" r="32" fill="#fff" stroke="var(--ring)" stroke-width="5"/><circle cx="36" cy="36" r="20" fill="var(--orange)"/><path d="M20 30 L52 42 M24 50 L48 22" stroke="#fff" stroke-width="3"/></svg>
  <section class="feature" style="top:1701px"><h2>NOODLING</h2><p>Net we hit the noodling field to try and find our own opal. With our expert guide showing you how to find opal, you’ll be a pro in no time.</p></section>

  <svg class="feature-icon" style="top:1863px" viewBox="0 0 72 72"><circle cx="36" cy="36" r="32" fill="#fff" stroke="var(--ring)" stroke-width="5"/><circle cx="36" cy="30" r="9" fill="var(--orange)"/><rect x="33" y="38" width="6" height="16" fill="var(--orange)"/></svg>
  <section class="feature" style="top:1852px"><h2>OPAL CUTTING AND POLISHING</h2><p>We’ll finish up our tour with an opal cutting and polishing demostration and who knows?It might be&nbsp; your opal we cut &amp; polish</p></section>

  <svg class="camping-banner" viewBox="0 0 1087 210"><polygon points="0,0 1087,0 1087,167 0,210" fill="url(#bannerTone)"/></svg>
  <p class="camping-text">FREE UNPOWERED CAMPING AT TOLMA'S WITH ALL TOURS<br>AS WELL AS DISCOUNTS ON POWERED CAMPING</p>
  <p class="camping-link">http://rest-belowground.example.au</p>

  <div class="brand">Wander<br>With Us</div>

  <ul class="contacts">
    <li><svg viewBox="0 0 26 26"><circle cx="13" cy="13" r="12" fill="var(--orange)"/><path d="M8 7 l3 0 l1 4 l-2 1 a8 8 0 0 0 4 4 l1 -2 l4 1 l0 3 a11 11 0 0 1 -11 -11z" fill="#fff"/></svg>0855501234</li>
    <li><svg viewBox="0 0 26 26"><circle cx="13" cy="13" r="12" fill="var(--orange)"/><rect x="7" y="9" width="12" height="8" fill="#fff"/></svg>hello@wanderwithus.example</li>
    <li><svg viewBox="0 0 26 26"><circle cx="13" cy="13" r="12" fill="var(--orange)"/><circle cx="13" cy="13" r="7" fill="none" stroke="#fff" stroke-width="2"/><path d="M6 13 H20 M13 6 V20" stroke="#fff" stroke-width="2"/></svg>www.wanderwithus.outback.example</li>
  </ul>

  <div class="follow-bar">Follow us<span class="social"></span><span class="social"></span></div>
</main>
</body>
</html>
```